Business Card Design

I need a business card design for my law office based in Pasadena, California. I am a sole practitioner and I specialize in business transaction and litigation, probate and estate planning, taxation law, corporate and business formation, immigration and real estate. I want something that is simple, yet stands out.

A friend helped to create a logo about 6 years ago. I am open to new ideas to changing the logo.

Industry/Entity Type

Business

Contact Information for Business Card

Law Offices of Doran M. Vaske
482 W. Harlow Ave., Suite 312
Pasadena, CA 91108
Tel: 626-503-7719
Fax: 626-581-9046
Email: dvaske@dmvlegalgrp.example

Attorney: Doran M. Vaske

```html
<!DOCTYPE html>
<html lang="en">
<head>
<meta charset="utf-8">
<title>Business Card – Law Offices of Doran M. Vaske</title>
<link href="https://fonts.googleapis.com/css2?family=Tinos:wght@400;700&family=Arimo:wght@400&display=swap" rel="stylesheet">
<style>
  :root {
    --page-bg: #e9e6e1;
    --card-white: #ffffff;
    --card-black: #2b2a2b;
    --ink: #2a2a2a;
    --rule: #7a7a7a;
    --on-dark: #f2f2f2;
    --on-dark-muted: #d9d9d9;
  }
  * { box-sizing: border-box; margin: 0; padding: 0; }
  html, body {
    width: 1200px; height: 902px; overflow: hidden;
    background: var(--page-bg);
  }
  .card {
    position: absolute; left: 100px; top: 165px;
    width: 1000px; height: 572px;
    background: var(--card-white);
    box-shadow: 0 10px 30px rgba(0,0,0,0.25);
    overflow: hidden;
  }
  .card-shape { position: absolute; inset: 0; }
  .brand {
    position: absolute; left: 260px; top: 60px; width: 480px;
    text-align: center;
  }
  .brand-mark {
    display: block; width: 84px; height: 84px; margin: 0 auto 28px;
    background: var(--card-black);
  }
  .brand-rule { height: 1px; background: var(--rule); }
  .brand-name {
    font-family: "Tinos", serif; font-weight: 400;
    font-size: 28px; letter-spacing: 3px; color: var(--ink);
    padding: 12px 0;
  }
  .contact-list {
    position: absolute; left: 618px; top: 292px;
    border-left: 2px solid var(--on-dark-muted);
    padding-left: 14px; list-style: none;
  }
  .contact-item {
    display: flex; align-items: center; gap: 16px;
    height: 40px;
    font-family: "Arimo", sans-serif; font-size: 23px; color: var(--on-dark);
  }
  .contact-icon { width: 20px; height: 20px; flex: none; }
  .holder {
    position: absolute; left: 60px; top: 408px;
    font-family: "Tinos", serif; color: var(--on-dark);
  }
  .holder-name { font-size: 46px; font-weight: 700; line-height: 1.05; }
  .holder-title { font-size: 30px; font-weight: 700; line-height: 1.1; }
  .address {
    position: absolute; right: 50px; bottom: 36px;
    font-family: "Arimo", sans-serif; font-size: 21px; color: var(--on-dark);
  }
</style>
</head>
<body>
  <div class="card">
    <svg class="card-shape" viewBox="0 0 1000 572" width="1000" height="572" aria-hidden="true">
      <path d="M0,310 C250,420 600,380 1000,40 L1000,572 L0,572 Z" fill="var(--card-black)"/>
      <path d="M140,370 C380,410 700,330 1000,8 L1000,22 C700,350 380,420 140,370 Z" fill="var(--card-black)"/>
    </svg>

    <div class="brand">
      <span class="brand-mark"></span>
      <div class="brand-rule"></div>
      <div class="brand-name">LAW OFFICES OF DORAN M. VASKE</div>
      <div class="brand-rule"></div>
    </div>

    <ul class="contact-list">
      <li class="contact-item">
        <svg class="contact-icon" viewBox="0 0 20 20"><rect x="1" y="1" width="18" height="18" rx="2" fill="var(--on-dark)"/><path d="M6 5c1 3 3 6 8 9l1-2-3-2-1 1c-2-1-3-2-4-4l1-1-1-3z" fill="var(--card-black)"/></svg>
        <span>626-503-7719</span>
      </li>
      <li class="contact-item">
        <svg class="contact-icon" viewBox="0 0 20 20"><rect x="1" y="1" width="18" height="18" rx="2" fill="var(--on-dark)"/><rect x="5" y="5" width="10" height="10" fill="var(--card-black)"/><rect x="7" y="7" width="6" height="2" fill="var(--on-dark)"/></svg>
        <span>626-581-9046</span>
      </li>
      <li class="contact-item">
        <svg class="contact-icon" viewBox="0 0 20 20"><rect x="1" y="1" width="18" height="18" rx="2" fill="var(--on-dark)"/><rect x="4" y="6" width="12" height="8" fill="none" stroke="var(--card-black)" stroke-width="1.5"/><path d="M4 6l6 5 6-5" fill="none" stroke="var(--card-black)" stroke-width="1.5"/></svg>
        <span>dvaske@dmvlegalgrp.example</span>
      </li>
      <li class="contact-item">
        <svg class="contact-icon" viewBox="0 0 20 20"><rect x="1" y="1" width="18" height="18" rx="2" fill="var(--on-dark)"/><circle cx="10" cy="10" r="5.5" fill="none" stroke="var(--card-black)" stroke-width="1.5"/><path d="M4.5 10h11M10 4.5v11" stroke="var(--card-black)" stroke-width="1.2"/></svg>
        <span>www.dmvlegalgrp.example</span>
      </li>
    </ul>

    <div class="holder">
      <div class="holder-name">Doran M. Vaske</div>
      <div class="holder-title">Attorney</div>
    </div>

    <div class="address">482 W. Harlow Ave., Suite 312 Pasadena, CA 91108</div>
  </div>
</body>
</html>
```